Certificate Design for Employee Loyalty

We're a digital marketing agency in Australia (www.brightkitestudio.com.au) and we're looking to create a design for a certificate to celebrate employees who reach 5 years with us (we have a few coming up soon).
Ideally we'd want something that captures our funky, digital agency culture (see our Facebook page www.facebook.com/brightkitestudio for what we mean) and not be too "corporatey"
A4 portrait or landscape designs would be awesome, with spots for employee's name, a brief 2-3 line message and a design that reflects our culture and the 5 year milestone for the employee.
Any questions, please post!
Target Market(s)
Digital marketing employees.

```html
<!DOCTYPE html>
<html lang="en">
<head>
<meta charset="utf-8">
<title>Certificate of Achievement – Employee Loyalty</title>
<link rel="stylesheet" href="https://fonts.googleapis.com/css2?family=Cormorant+Garamond:wght@500;600&family=Great+Vibes&family=Quicksand:wght@300;400&family=Didact+Gothic&display=swap">
<style>
  :root {
    --page-bg: #7d7e82;
    --card: #a9aaae;
    --card-edge: #6f7074;
    --frame-light: #c9cacd;
    --ink: #111111;
    --ink-soft: #2b2b2b;
    --placeholder-text: #cfd0d3;
    --rule: #7c7d81;
    --accent-blue: #2d7bb8;
    --band-dark: #050505;
    --band-mid: #5a5a5a;
  }
  * { box-sizing: border-box; margin: 0; padding: 0; }
  html, body { width: 1200px; height: 844px; overflow: hidden; background: var(--page-bg); }
  .certificate {
    position: relative;
    width: 1200px; height: 844px;
    background: var(--card);
    border: 4px solid var(--card-edge);
    box-shadow: inset 0 0 0 3px var(--frame-light), inset 0 0 0 6px var(--card-edge);
    overflow: hidden;
  }
  .title {
    position: absolute; top: 40px; left: 0; width: 100%;
    text-align: center;
    font-family: "Cormorant Garamond", serif;
    font-weight: 600; font-size: 100px; line-height: 1;
    color: var(--ink); letter-spacing: 1px;
    text-shadow: 0 1px 0 rgba(255,255,255,.25);
  }
  .band {
    position: absolute; left: 12px; right: 12px;
    background: linear-gradient(90deg, var(--band-mid) 0%, var(--band-dark) 18%, var(--band-dark) 82%, var(--band-mid) 100%);
  }
  .band--top { top: 147px; height: 31px; }
  .band--bottom { top: 792px; height: 14px; }
  .band-line {
    position: absolute; left: 12px; right: 12px; height: 2px;
    background: linear-gradient(90deg, transparent, var(--band-dark) 10%, var(--band-dark) 90%, transparent);
  }
  .band-line--bottom { top: 812px; }
  .connector {
    position: absolute; top: 124px; left: 0; width: 100%;
    text-align: center;
    font-family: "Great Vibes", cursive;
    font-size: 66px; line-height: 1; color: #ffffff;
  }
  .award-name {
    position: absolute; top: 192px; left: 0; width: 100%;
    text-align: center;
    font-family: "Didact Gothic", sans-serif;
    font-weight: 400; font-size: 74px; line-height: 1; color: var(--ink);
  }
  .recipient {
    position: absolute; top: 284px; left: 0; width: 100%;
    text-align: center;
    font-family: "Quicksand", sans-serif; font-weight: 300;
    font-size: 38px; line-height: 1; color: var(--placeholder-text);
  }
  .recipient-rule {
    position: absolute; top: 339px; left: 278px; width: 652px; height: 2px;
    background: var(--rule);
  }
  .milestone {
    position: absolute; top: 344px; left: 0; width: 100%;
    text-align: center;
    font-family: "Quicksand", sans-serif; font-weight: 400;
    font-size: 34px; line-height: 1; color: var(--accent-blue); letter-spacing: 1px;
  }
  .flourish {
    position: absolute; top: 385px; left: 380px; width: 460px; height: 120px;
    background: radial-gradient(ellipse at center, rgba(20,20,20,.28) 0%, rgba(20,20,20,.12) 45%, rgba(20,20,20,0) 72%);
  }
  .message-lines { position: absolute; left: 410px; width: 396px; top: 530px; }
  .message-line { height: 2px; background: var(--rule); margin-bottom: 45px; }
  .team-figures {
    position: absolute; left: 66px; top: 403px; width: 300px; height: 378px;
    background: linear-gradient(180deg, #1a1a1a 0%, #050505 100%);
    border-radius: 90px 90px 14px 14px;
    opacity: .92;
  }
  .studio-name {
    position: absolute; top: 702px; left: 0; width: 100%;
    display: flex; justify-content: center; align-items: center; gap: 14px;
    font-family: "Quicksand", sans-serif; font-weight: 400;
    font-size: 44px; line-height: 1; color: var(--ink-soft);
  }
  .studio-dot {
    width: 18px; height: 18px; border-radius: 50%; background: var(--accent-blue);
  }
  .seal-area {
    position: absolute; left: 872px; top: 480px; width: 270px; height: 270px;
    border-radius: 50%;
    background: radial-gradient(circle at 40% 40%, #d8d8da 0%, #8e8e92 55%, #4a4a4e 100%);
  }
</style>
</head>
<body>
  <main class="certificate">
    <h1 class="title">Certificate of Achievement</h1>
    <div class="band band--top"></div>
    <p class="connector">for</p>
    <h2 class="award-name">Employee Loyalty</h2>
    <p class="recipient">(Name)</p>
    <div class="recipient-rule"></div>
    <p class="milestone">soaring for 5 years</p>
    <div class="flourish" role="img" aria-label="Decorative black scroll flourish beneath the name line"></div>

    <div class="message-lines">
      <div class="message-line"></div>
      <div class="message-line"></div>
      <div class="message-line"></div>
    </div>

    <div class="team-figures" role="img" aria-label="Black silhouettes of three colleagues standing together"></div>

    <div class="studio-name"><span class="studio-dot"></span><span>Bright Kite Studio</span></div>

    <div class="seal-area" role="img" aria-label="Round silver award seal"></div>

    <div class="band band--bottom"></div>
    <div class="band-line band-line--bottom"></div>
  </main>
</body>
</html>
```